church business card design

we have a logo and would like our business card to complement the logo. we would prefer the logo in white on a coloured background - probably blue. Under the logo or near it we would have the Words 'Love God. Love people. Follow Jesus.'
We would like some yellow/gold highlights. We like the design by mintaro quill 4821 front of card - https://www.pelvarostudio.com/businesscard-design/contest/5812094

Our church is multicultural, inner city, friendly, warm welcoming and that's the feel we would like. there's also an element of being spontaneous, so a swirl or swoosh might help give that feel. the example card above had some curved shapes on the front of the card for example.
on the second side of the card would have the details of the Senior Pastor and the contact details for the church.
after the business card we would be looking at letterhead and an A5 flyer for printing but also as document templates so we can create invitations etc going forward

```html
<!DOCTYPE html>
<html lang="en">
<head>
<meta charset="utf-8">
<title>Harbor Stone Church – Business Card</title>
<link href="https://fonts.googleapis.com/css2?family=Exo+2:wght@400;500;700&display=swap" rel="stylesheet">
<style>
  :root {
    --page-bg: #e6e2dc;
    --navy-light: #2a2b40;
    --navy-dark: #07070f;
    --gold-light: #c0841a;
    --gold-dark: #8a520c;
    --cross: #cdb89a;
    --white: #f4f4f4;
    --tagline-gold: #b8924f;
    --ink: #141012;
  }
  * { margin: 0; padding: 0; box-sizing: border-box; }
  html, body {
    width: 1200px; height: 969px; overflow: hidden;
    background: var(--page-bg);
    font-family: "Exo 2", sans-serif;
  }
  .card {
    position: absolute; left: 166px; top: 237px;
    width: 867px; height: 494px;
    display: flex;
    box-shadow: 0 10px 30px rgba(0,0,0,0.25);
  }
  .card-front {
    position: relative; width: 465px; height: 100%;
    background: radial-gradient(ellipse at 50% 75%, var(--navy-light) 0%, #141426 45%, var(--navy-dark) 100%);
  }
  .card-back {
    position: relative; flex: 1; height: 100%;
    background: linear-gradient(160deg, var(--gold-light) 0%, #a86c12 55%, var(--gold-dark) 100%);
  }
  .cross { position: absolute; left: 441px; top: 28px; width: 52px; height: 466px; z-index: 2; }
  .church-name {
    position: absolute; left: 0; width: 465px; top: 186px;
    text-align: center; color: var(--white);
    font-weight: 700; font-size: 44px; line-height: 1.05; letter-spacing: 2px;
    text-transform: uppercase;
  }
  .church-name .sub { display: block; font-size: 22px; letter-spacing: 18px; margin-top: 10px; padding-left: 18px; }
  .tagline-rule {
    position: absolute; left: 74px; top: 300px; width: 316px; height: 1px;
    background: var(--tagline-gold); opacity: 0.7;
  }
  .tagline {
    position: absolute; left: 0; width: 465px; top: 304px;
    text-align: center; color: var(--tagline-gold); font-size: 17px;
  }
  .details { position: absolute; left: 66px; top: 124px; color: var(--ink); }
  .details .name { font-weight: 700; font-size: 32px; letter-spacing: 0.5px; line-height: 1.1; }
  .details .role { font-size: 21px; line-height: 1.2; }
  .details .address { font-size: 20px; line-height: 1.35; margin-top: 18px; }
  .contact-list { list-style: none; margin-top: 14px; }
  .contact-list li { display: flex; align-items: center; font-size: 20px; line-height: 27.5px; }
  .contact-list svg { width: 16px; height: 16px; margin-right: 12px; fill: var(--ink); }
</style>
</head>
<body>
  <div class="card">
    <section class="card-front">
      <div class="church-name">Harbor Stone<span class="sub">Church</span></div>
      <div class="tagline-rule"></div>
      <div class="tagline">Seek Grace • Serve Others • Walk in Faith</div>
    </section>
    <svg class="cross" viewBox="0 0 52 466" aria-hidden="true">
      <rect x="20" y="0" width="12" height="466" fill="var(--cross)"/>
      <rect x="0" y="19" width="52" height="11" fill="var(--cross)"/>
    </svg>
    <section class="card-back">
      <div class="details">
        <div class="name">DANIEL REYES</div>
        <div class="role">Senior Pastor</div>
        <div class="address">2934 Cedarview Lane<br>Juneau, Alaska 99801</div>
        <ul class="contact-list">
          <li><svg viewBox="0 0 16 16"><path d="M3 1l3 3-1.5 2a9 9 0 0 0 5.5 5.5L12 10l3 3-2 2C7 15 1 9 1 3z"/></svg>555-214-3870</li>
          <li><svg viewBox="0 0 16 16"><rect x="4" y="2" width="8" height="5"/><rect x="1" y="7" width="14" height="7" rx="1"/></svg>555-214-3871</li>
          <li><svg viewBox="0 0 16 16"><path d="M1 4h14v9H1z M1 4l7 5 7-5" stroke="var(--gold-light)" stroke-width="1"/></svg>name@harborstone.org</li>
          <li><svg viewBox="0 0 16 16"><circle cx="8" cy="8" r="7"/><path d="M1 8h14M8 1c3 3 3 11 0 14M8 1c-3 3-3 11 0 14" stroke="var(--gold-light)" fill="none"/></svg>www.harborstone.org</li>
        </ul>
      </div>
    </section>
  </div>
</body>
</html>
```